Poster for a series of live music events

Looking for a simplistic poster design for live music gigs. I would like something that i can reuse by moving the positioning of the words on the poster and the colour scheme. Attached is an example of a design that i like. The size should be A4.
File format preferred would be photoshop.
Text in the poster is not that important at this stage as it is just a template i am after. But it should include band names, location, date and time. So feel free to make up the text. The file provided in the brief will show you the similar things that will be included.
Events

```html
<!DOCTYPE html>
<html lang="en">
<head>
<meta charset="utf-8">
<title>Musical Band – Live in Concert</title>
<link rel="stylesheet" href="https://fonts.googleapis.com/css2?family=Federo&family=Great+Vibes&family=Raleway:wght@300;400&family=Poppins:wght@700&display=swap">
<style>
  :root {
    --bg: #000000;
    --glow: #3a1d5c;
    --title: #f4ee10;
    --white: #ffffff;
    --date: #e3131c;
    --address: #f0e91a;
    --rule-light: #e8e8e8;
    --rule-dark: #5a5a5a;
    --swirl-violet: #6a3aa8;
    --swirl-cyan: #2fb6d6;
    --swirl-pink: #e0407a;
    --swirl-amber: #f0a020;
    --swirl-lime: #9cc43a;
  }
  * { margin: 0; padding: 0; box-sizing: border-box; }
  html, body { width: 849px; height: 1200px; overflow: hidden; background: var(--bg); }
  .poster {
    position: relative;
    width: 849px;
    height: 1200px;
    overflow: hidden;
    background:
      radial-gradient(ellipse 430px 380px at 410px 420px, var(--glow) 0%, rgba(40,18,66,0.55) 45%, rgba(0,0,0,0) 100%),
      var(--bg);
    font-family: "Raleway", sans-serif;
    color: var(--white);
  }
  .band-name {
    position: absolute;
    top: 160px;
    left: 0;
    width: 849px;
    text-align: center;
    font-family: "Federo", sans-serif;
    font-size: 104px;
    line-height: 1;
    color: var(--title);
    letter-spacing: -1px;
    transform: scaleY(1.18);
    text-shadow: 0 0 18px rgba(0,0,0,0.6);
  }
  .music-swirl {
    position: absolute;
    top: 300px;
    left: 0;
    width: 849px;
    height: 400px;
    background:
      radial-gradient(ellipse 120px 90px at 720px 130px, rgba(47,182,214,0.55), rgba(47,182,214,0) 100%),
      radial-gradient(ellipse 110px 80px at 480px 260px, rgba(224,64,122,0.45), rgba(224,64,122,0) 100%),
      radial-gradient(ellipse 100px 70px at 250px 340px, rgba(240,160,32,0.40), rgba(240,160,32,0) 100%),
      radial-gradient(ellipse 90px 80px at 570px 170px, rgba(156,196,58,0.40), rgba(156,196,58,0) 100%),
      radial-gradient(ellipse 120px 160px at 90px 200px, rgba(106,58,168,0.55), rgba(106,58,168,0) 100%),
      radial-gradient(ellipse 420px 130px at 430px 250px, rgba(106,58,168,0.45), rgba(106,58,168,0) 100%);
  }
  .headline {
    position: absolute;
    top: 718px;
    left: 0;
    width: 849px;
    text-align: center;
    white-space: nowrap;
    line-height: 1;
  }
  .headline .live { font-family: "Raleway", sans-serif; font-weight: 300; font-size: 76px; }
  .headline .in { font-family: "Raleway", sans-serif; font-weight: 300; font-size: 38px; margin: 0 6px 0 10px; }
  .headline .concert { font-family: "Great Vibes", cursive; font-size: 104px; }
  .event-date {
    position: absolute;
    top: 845px;
    left: 0;
    width: 849px;
    text-align: center;
    font-family: "Raleway", sans-serif;
    font-weight: 400;
    font-size: 30px;
    color: var(--date);
  }
  .divider {
    position: absolute;
    top: 901px;
    left: 0;
    width: 849px;
    height: 14px;
    background: linear-gradient(to bottom, var(--rule-light) 0%, #bdbdbd 45%, var(--rule-dark) 100%);
  }
  .info {
    position: absolute;
    top: 952px;
    font-family: "Raleway", sans-serif;
    font-weight: 400;
    font-size: 31px;
    line-height: 1;
  }
  .info.entry { left: 114px; }
  .info.doors { left: 502px; }
  .venue-mark {
    position: absolute;
    top: 1056px;
    left: 0;
    width: 849px;
    display: flex;
    justify-content: center;
    align-items: center;
    gap: 8px;
    font-family: "Raleway", sans-serif;
    font-weight: 400;
    font-size: 16px;
    color: var(--white);
  }
  .venue-mark .dot {
    width: 20px;
    height: 20px;
    border: 1.5px solid var(--white);
    border-radius: 50%;
  }
  .address {
    position: absolute;
    top: 1118px;
    left: 0;
    width: 849px;
    text-align: center;
    font-family: "Poppins", sans-serif;
    font-weight: 700;
    font-size: 18px;
    color: var(--address);
  }
</style>
</head>
<body>
  <main class="poster">
    <h1 class="band-name">Musical Band</h1>

    <div class="music-swirl" role="img" aria-label="Colourful swirl of musical notes and clefs flowing along a purple staff"></div>

    <p class="headline"><span class="live">Live</span><span class="in">in</span><span class="concert">Concert</span></p>
    <p class="event-date">05.04.2015</p>

    <div class="divider"></div>

    <p class="info entry">$ 5 entry</p>
    <p class="info doors">Doors: 7:30 pm</p>

    <div class="venue-mark"><span class="dot"></span><span>Lantern Yard</span></div>

    <p class="address">The Old Copper Mill, 42 Lantern Row, London E9 2XP</p>
  </main>
</body>
</html>
```